Brivane - Business Cards for a new venture

create business card for a startup classified business dealing in construction materials, the cards need to have a professional look but modern, more serious than playful, one of the samples must include the official font (attached), please explore using the official colors in the company's logo

Target Market(s)

Energy sector

Contact Information for Business Card

Font styles to use
Other font styles liked:
• suissnord

Requirements
Must have
• corporate colors (in logo attached)
Nice to have
• Official font (in one of the samples) font is : suissnord
Should not have
• Cartoonish look

```html
<!DOCTYPE html>
<html lang="en">
<head>
<meta charset="utf-8">
<title>Brivane – Business Cards</title>
<link rel="stylesheet" href="https://fonts.googleapis.com/css2?family=Michroma&family=Questrial&display=swap">
<style>
  :root {
    --navy: #0d4a7c;
    --steel: #96999c;
    --ink: #0d3f6e;
    --paper: #ffffff;
    --stage: #000000;
    --page: #ffffff;
  }
  * { margin: 0; padding: 0; box-sizing: border-box; }
  html, body { width: 969px; height: 1200px; overflow: hidden; background: var(--page); }
  .canvas { position: relative; width: 969px; height: 1200px; }
  .stage { position: absolute; left: 73px; top: 0; width: 896px; height: 941px; background: var(--stage); }
  .card {
    position: absolute; left: 223px; width: 601px; height: 344px;
    background: var(--paper); border-radius: 16px; overflow: hidden;
  }
  .card--front { top: 115px; }
  .card--back { top: 525px; }

  .edge-band { position: absolute; top: 0; height: 100%; }
  .edge-band--left {
    left: 0; width: 104px;
    background: linear-gradient(90deg, var(--navy) 0%, var(--navy) 45%, var(--steel) 100%);
  }
  .edge-band--right {
    right: 0; width: 104px;
    background: linear-gradient(270deg, var(--navy) 0%, var(--navy) 45%, var(--steel) 100%);
  }
  .corner-block {
    position: absolute; left: 0; top: 0; width: 220px; height: 100%;
    background: linear-gradient(160deg, var(--navy) 0%, var(--navy) 50%, var(--steel) 100%);
  }

  .brand-name {
    position: absolute; left: 0; right: 0; top: 200px; text-align: center;
    font-family: "Michroma", sans-serif; font-size: 27px; letter-spacing: 5px;
    color: var(--steel);
  }

  .holder { position: absolute; right: 37px; top: 40px; text-align: right; }
  .holder__name {
    font-family: "Michroma", sans-serif; font-size: 26px; line-height: 1;
    letter-spacing: 1px; color: var(--navy);
  }
  .holder__role {
    margin-top: 5px; font-family: "Questrial", sans-serif; font-size: 17.5px;
    letter-spacing: 0.6px; color: var(--steel);
  }

  .contacts { position: absolute; right: 0; top: 0; width: 100%; height: 100%; list-style: none; }
  .contact {
    position: absolute; right: 116px; transform: translateY(-50%);
    font-family: "Questrial", sans-serif; font-size: 17px; color: var(--ink); white-space: nowrap;
  }
  .contact--mobile { top: 161px; }
  .contact--office { top: 198px; }
  .contact--email { top: 235px; }
  .contact--address { top: 273px; right: 121px; }

  .icon { position: absolute; width: 24px; height: 24px; left: 505px; transform: translateY(-50%); }
  .icon path, .icon rect, .icon circle { fill: none; stroke: var(--steel); stroke-width: 1.4; stroke-linejoin: round; stroke-linecap: round; }
  .icon--mobile { top: 161px; }
  .icon--office { top: 198px; }
  .icon--email { top: 235px; }
  .icon--address { top: 273px; }

  .contact-rule { position: absolute; left: 561px; top: 141px; width: 2.5px; height: 158px; background: var(--navy); }
</style>
</head>
<body>
<main class="canvas">
  <div class="stage"></div>

  <section class="card card--front" aria-label="Business card front">
    <div class="edge-band edge-band--left" role="img" aria-label="Navy and grey decorative panel on the left edge"></div>
    <div class="edge-band edge-band--right" role="img" aria-label="Navy and grey decorative panel on the right edge"></div>
    <p class="brand-name">BRIVANE</p>
  </section>

  <section class="card card--back" aria-label="Business card back">
    <div class="corner-block" role="img" aria-label="Navy and grey decorative panel on the left side"></div>

    <div class="holder">
      <p class="holder__name">NAME</p>
      <p class="holder__role">DESIGNATION</p>
    </div>

    <ul class="contacts">
      <li class="contact contact--mobile">mobile number</li>
      <li class="contact contact--office">office number</li>
      <li class="contact contact--email">youremail@mailbox.com</li>
      <li class="contact contact--address">your address</li>
    </ul>

    <svg class="icon icon--mobile" viewBox="0 0 24 24" aria-hidden="true">
      <rect x="6.5" y="1.5" width="11" height="21" rx="2"/>
      <path d="M6.5 5 H17.5 M6.5 19 H17.5"/>
    </svg>
    <svg class="icon icon--office" viewBox="0 0 24 24" aria-hidden="true">
      <path d="M5 3 L8.5 3 L10 8 L8 9.5 Q10 14 14.5 16 L16 14 L21 15.5 L21 19 Q20 21 17.5 21 Q10 20 5.5 12 Q3 7 5 3 Z"/>
    </svg>
    <svg class="icon icon--email" viewBox="0 0 24 24" aria-hidden="true">
      <rect x="1.5" y="5" width="21" height="14"/>
      <path d="M1.5 5 L12 13.5 L22.5 5 M1.5 19 L9.5 11.5 M22.5 19 L14.5 11.5"/>
    </svg>
    <svg class="icon icon--address" viewBox="0 0 24 24" aria-hidden="true">
      <path d="M12 23 Q4.5 14 4.5 9 A7.5 7.5 0 0 1 19.5 9 Q19.5 14 12 23 Z"/>
      <circle cx="12" cy="9" r="2.8"/>
    </svg>

    <div class="contact-rule"></div>
  </section>
</main>
</body>
</html>
```